Meridian Rest Supply Needs Business Card

Looking for a very nice looking business card. Creative but not extravagant. We sell beds and pillows across the U.S. and need something professional but catchy. I have attached the logo.

Name : Dale Fenwick
Title : President
Phone : (800) 417-2964
Email: sleep@quorvana.com
Website: www.quorvana.com

Can be single-sided or double-sided
horizontal or vertical

Can use Blues/Greys

Target Market(s)

Mass Market

Industry/Entity Type

Retail

Contact Information for Business Card

Name : Dale Fenwick
Title : President
Phone : (800) 417-2964
Email: sleep@quorvana.com
Website: www.quorvana.com

Requirements
Must have
• Clean, Modern, Smooth
• Can use Blues/Greys
• On the other side without the information - have something simple like www.quorvana.com or our logo
Nice to have
• Surprise me
Should not have
• Nothing crazy, nothing cluttered

```html
<!DOCTYPE html>
<html lang="en">
<head>
<meta charset="utf-8">
<title>Quorvana Business Card</title>
<link href="https://fonts.googleapis.com/css2?family=Montserrat:wght@400;500&display=swap" rel="stylesheet">
<style>
  :root {
    --brand-blue: #37a5da;
    --text-grey: #6f757b;
    --rule-blue: #9fd2ec;
    --card-white: #ffffff;
    --page-bg: #e9eaec;
  }
  * { margin: 0; padding: 0; box-sizing: border-box; }
  html, body {
    width: 1200px; height: 834px; overflow: hidden;
    background: var(--page-bg);
    font-family: "Montserrat", sans-serif;
  }
  .stage {
    width: 1200px; height: 834px;
    display: flex; justify-content: center; align-items: center; gap: 80px;
  }
  .card {
    width: 400px; height: 700px; position: relative;
    box-shadow: 0 6px 24px rgba(0,0,0,0.12);
  }
  .card-front { background: var(--card-white); }
  .card-back {
    background: var(--brand-blue);
    display: flex; justify-content: center; align-items: center;
  }
  .company-name {
    font-family: "Montserrat", sans-serif;
    font-weight: 500;
    color: var(--brand-blue);
    line-height: 1;
  }
  .card-front .company-name {
    position: absolute; top: 52px; right: 38px; font-size: 34px;
  }
  .card-back .company-name { color: var(--card-white); font-size: 54px; }
  .identity { position: absolute; left: 40px; top: 300px; }
  .person-name {
    font-size: 26px; font-weight: 500; color: var(--brand-blue);
    letter-spacing: 1px; text-transform: uppercase; line-height: 1;
  }
  .person-title {
    font-size: 12px; font-weight: 500; color: var(--text-grey);
    letter-spacing: 1px; text-transform: uppercase; margin-top: 4px;
  }
  .contact-list {
    position: absolute; left: 40px; top: 400px; width: 240px;
    list-style: none;
  }
  .contact-row {
    display: flex; align-items: flex-start; gap: 18px;
    padding: 12px 0 14px;
    border-bottom: 2px solid var(--rule-blue);
  }
  .contact-icon {
    width: 34px; height: 34px; flex: none;
    border: 2.5px solid var(--brand-blue); border-radius: 7px;
    display: flex; justify-content: center; align-items: center;
  }
  .contact-text {
    font-size: 15px; font-weight: 400; color: var(--text-grey); line-height: 1.35;
    padding-top: 6px;
  }
</style>
</head>
<body>
<main class="stage">
  <section class="card card-front">
    <div class="company-name">Quorvana</div>
    <div class="identity">
      <p class="person-name">Dale Fenwick</p>
      <p class="person-title">President</p>
    </div>
    <ul class="contact-list">
      <li class="contact-row">
        <span class="contact-icon">
          <svg width="18" height="18" viewBox="0 0 24 24" aria-hidden="true"><path d="M6.6 3.5l3 3.2-1.8 2.4a12 12 0 0 0 7.1 7.1l2.4-1.8 3.2 3-1.6 3A16 16 0 0 1 3.6 5.1z" fill="none" stroke="#37a5da" stroke-width="2.2" stroke-linejoin="round"/></svg>
        </span>
        <span class="contact-text">(800) 417-2964</span>
      </li>
      <li class="contact-row">
        <span class="contact-icon">
          <svg width="18" height="18" viewBox="0 0 24 24" aria-hidden="true"><rect x="3" y="6" width="18" height="12" rx="1.5" fill="none" stroke="#37a5da" stroke-width="2.2"/><path d="M3.5 7l8.5 6.5L20.5 7" fill="none" stroke="#37a5da" stroke-width="2.2"/></svg>
        </span>
        <span class="contact-text">sleep@quorvana.com<br>www.quorvana.com</span>
      </li>
      <li class="contact-row">
        <span class="contact-icon">
          <svg width="18" height="18" viewBox="0 0 24 24" aria-hidden="true"><path d="M3 11.5L12 4l9 7.5M6 10v10h12V10" fill="none" stroke="#37a5da" stroke-width="2.2" stroke-linejoin="round"/><rect x="10" y="14" width="4" height="6" fill="#37a5da"/></svg>
        </span>
        <span class="contact-text">18 Linden Row<br>Portland 97205</span>
      </li>
    </ul>
  </section>
  <section class="card card-back">
    <div class="company-name">Quorvana</div>
  </section>
</main>
</body>
</html>
```